Trifold brochure for Thai yoga massage practice (In a Combat gym and a Spa)

I am a Practitioner of Thai massage in Toronto, and will in the near future be offering personal training with transitional fitness from couch potato to weekend warriors.

I train in Muay-thai and my current stream of clients are "thai tigers" in need of restorative therapy to get them back on their feet - hence the website name Fernquiet.com.
My other stream of clients are in a Lovely Spa on a rooftop patio (if you're ever in Toronto come on by).

So I have the best of two worlds (injuries vs. pure bliss) Dark vs. Light

I want to introduce Thai yoga massage to a new modern audience. Thai massage is an ancient, effective hybrid therapy incorporating traditional acupressure/ body meridian therapy and human kinetics simultaneously.

Brochures are meant for distribution to martial arts studios, fitness gyms and other spas.

I am open to eye-catching, out of the box ideas.

My website: www.fernquiet.com (I am in the process of editing this new web space - apologies for the very basic nature of it)

Pictures are attached for review or view my link:
https://files.plumdock.net/share?id=7QX41mKpLw93_rTbNvEhYcUaZdJ2&view=open

Thank you!

Target Market(s)

20-45 year old fitness enthusiast for a gym audience
or 20-55 year old looking for general wellness/ relaxation
or combination of both (yin/yang type design)

Industry/Entity Type

Training

Font styles to use
Decorative

Requirements
Must have
• Will be looking for innovation, clever, witty design, please be creative. Toronto is a quirky city, I welcome quirky, yet tasteful designs.

Please use a good amount of flow, and streaming lines.
Nice to have
• If we could have a yin / yang effect that would be nice (Combat restoration vs. Relaxation)
Should not have
• Please do not have text / designs that convey the stereotypical nonsense that surround Asian based massage (my cup is full already).

```html
<!DOCTYPE html>
<html lang="en">
<head>
<meta charset="utf-8">
<title>Fernquiet – Brochure Spread</title>
<link rel="stylesheet" href="https://fonts.googleapis.com/css2?family=Open+Sans:wght@400;600;700&display=swap">
<style>
  :root {
    --backdrop: #dcdad5;
    --paper: #ffffff;
    --plum: #8e1a4e;
    --magenta: #b3125c;
    --pink-pale: #e9a9c7;
    --body-text: #5a5a5a;
    --wall-dark: #26262b;
    --wall-mid: #34333a;
    --floor-red: #8a2630;
    --mat-purple: #4a3f7e;
    --lead-yellow: #ffe24a;
    --lead-purple: #6a1668;
    --white: #ffffff;
  }
  * { box-sizing: border-box; margin: 0; padding: 0; }
  html, body {
    width: 1200px; height: 804px; overflow: hidden;
    background: var(--backdrop);
    font-family: "Open Sans", Arial, sans-serif;
  }
  .spread {
    position: absolute; left: 40px; top: 22px;
    width: 1120px; height: 760px;
    display: flex;
    box-shadow: 0 10px 30px rgba(0,0,0,.18);
  }
  .page {
    position: relative; width: 560px; height: 760px;
    background: var(--paper); overflow: hidden;
  }
  .page-waves { position: absolute; inset: 0; width: 560px; height: 760px; }

  /* Left page */
  .intro-title {
    position: absolute; left: 45px; top: 50px;
    font-size: 34px; font-weight: 700; color: var(--plum);
  }
  .intro-body {
    position: absolute; left: 45px; top: 112px; width: 470px;
    font-size: 10.5px; line-height: 1.6; color: var(--body-text);
    text-align: justify;
  }
  .intro-body p + p { margin-top: 14px; }

  .photo-circle {
    position: absolute; border-radius: 50%;
    border: 5px solid var(--white);
    background:
      radial-gradient(circle at 40% 35%, rgba(255,255,255,.08), transparent 55%),
      linear-gradient(180deg, var(--wall-dark) 0%, var(--wall-mid) 58%, var(--floor-red) 70%, var(--mat-purple) 84%, var(--wall-dark) 100%);
    box-shadow: 0 2px 6px rgba(0,0,0,.25);
  }
  .photo-circle--intro { left: 195px; top: 430px; width: 160px; height: 160px; }
  .photo-circle--desc { left: 408px; top: 548px; width: 112px; height: 112px; }

  .site-url {
    position: absolute; font-size: 11px; font-weight: 700; letter-spacing: 1.5px;
  }
  .site-url--intro { left: 0; width: 560px; top: 628px; text-align: center; color: var(--white); }
  .site-url--desc { left: 270px; top: 722px; color: var(--magenta); }

  .page-number { position: absolute; bottom: 14px; font-size: 11px; }
  .page-number--left { left: 16px; color: #f6dbe7; }
  .page-number--right { right: 18px; bottom: 28px; color: #777; }

  /* Right page */
  .session-photo {
    position: absolute; left: 0; top: 0; width: 560px; height: 600px;
    background:
      radial-gradient(ellipse 60% 45% at 62% 30%, rgba(255,255,255,.07), transparent 70%),
      linear-gradient(90deg, rgba(0,0,0,.18) 0%, transparent 30%, transparent 70%, rgba(0,0,0,.2) 100%),
      linear-gradient(180deg, var(--wall-mid) 0%, var(--wall-dark) 45%, #3b2a30 56%, var(--floor-red) 63%, #5a3550 70%, var(--mat-purple) 78%, var(--wall-dark) 100%);
  }
  .desc-title {
    position: absolute; left: 32px; top: 92px;
    font-size: 27px; font-weight: 700; color: var(--white);
  }
  .desc-col {
    position: absolute; font-size: 10.5px; line-height: 1.45; color: var(--white);
  }
  .desc-col--one { left: 70px; top: 468px; width: 185px; }
  .desc-col--two { left: 285px; top: 408px; width: 190px; }
  .lead { font-weight: 700; }
  .lead--yellow { color: var(--lead-yellow); }
  .lead--purple { color: var(--lead-purple); }
</style>
</head>
<body>
<main class="spread">

  <section class="page page--intro">
    <svg class="page-waves" viewBox="0 0 560 760" aria-hidden="true">
      <defs>
        <linearGradient id="magentaBand" x1="0" y1="0" x2="1" y2="0">
          <stop offset="0" stop-color="#b0165f"/>
          <stop offset=".55" stop-color="#c6134f"/>
          <stop offset="1" stop-color="#8f1557"/>
        </linearGradient>
      </defs>
      <path d="M0,455 C170,425 340,420 560,385 L560,425 C330,465 160,470 0,495 Z" fill="var(--pink-pale)"/>
      <path d="M0,440 C170,410 340,405 560,370 L560,385 C340,420 170,425 0,455 Z" fill="#f4d3e2"/>
      <path d="M0,495 C160,470 330,465 560,425 L560,760 L0,760 Z" fill="url(#magentaBand)"/>
      <path d="M0,690 C200,660 380,680 560,640 L560,675 C380,715 200,700 0,725 Z" fill="#ffffff" opacity=".35"/>
      <path d="M0,725 C200,700 380,715 560,675 L560,760 L0,760 Z" fill="#f3c7da" opacity=".7"/>
    </svg>

    <h1 class="intro-title">Introduction</h1>
    <div class="intro-body">
      <p>Fernquiet began on the mats of a busy fight gym, where sore shoulders and tight hips needed more than rest. Thai yoga massage blends slow pressure along the body lines with assisted stretching, so each session feels like a quiet conversation between breath and movement. Clients leave lighter, looser and ready to train again. Whether the week held heavy pad rounds or long runs, the work meets you where you are and helps you move with ease.</p>
      <p>The same hands also work high above the city in a calm rooftop spa. There the pace slows down, the music softens and the goal is simple rest. One practice, two worlds: recovery for hard working athletes and deep calm for anyone who simply needs a pause from a long and crowded week. Both rooms share one idea: the body heals best when it feels safe, warm and listened to, so nothing is rushed.</p>
      <p>Every session is shaped around your body on that day, whether you arrive bruised from sparring or tired from a desk. Wear loose clothing, bring water and come as you are. Sessions run sixty or ninety minutes and can be booked online. First visits include a short talk about old injuries, training habits and what you hope to feel when you stand up again.</p>
    </div>

    <div class="photo-circle photo-circle--intro" role="img" aria-label="Practitioner kneeling beside a client on a gym mat, guiding a leg stretch"></div>
    <p class="site-url site-url--intro">www.fernquiet.com</p>
    <span class="page-number page-number--left">2</span>
  </section>

  <section class="page page--description">
    <div class="session-photo" role="img" aria-label="Practitioner in red standing over a client lying on a gym floor, lifting the client's leg into a stretch"></div>

    <svg class="page-waves" viewBox="0 0 560 760" aria-hidden="true">
      <defs>
        <linearGradient id="sunsetBand" x1="0" y1="0" x2="1" y2="0">
          <stop offset="0" stop-color="#c8174f"/>
          <stop offset=".35" stop-color="#e4501f"/>
          <stop offset=".7" stop-color="#f5a01b"/>
          <stop offset="1" stop-color="#f8d51e"/>
        </linearGradient>
        <linearGradient id="sunsetFade" x1="0" y1="0" x2="0" y2="1">
          <stop offset="0" stop-color="#ffffff" stop-opacity="0"/>
          <stop offset="1" stop-color="#ffffff" stop-opacity=".25"/>
        </linearGradient>
      </defs>
      <path d="M0,430 C160,380 360,330 560,300 L560,360 C350,385 160,430 0,475 Z" fill="url(#sunsetBand)" opacity=".35"/>
      <path d="M0,475 C160,430 350,385 560,360 L560,560 L0,560 Z" fill="url(#sunsetBand)"/>
      <path d="M0,560 L560,560 L560,640 C400,610 200,640 0,700 Z" fill="url(#sunsetBand)"/>
      <path d="M0,475 C160,430 350,385 560,360 L560,640 C400,610 200,640 0,700 Z" fill="url(#sunsetFade)"/>
      <path d="M0,660 C200,605 400,585 560,610 L560,635 C400,612 200,640 0,690 Z" fill="#ffffff" opacity=".45"/>
      <path d="M0,700 C200,640 400,610 560,640 L560,760 L0,760 Z" fill="var(--paper)"/>
      <path d="M0,715 C200,670 400,650 560,670 L560,685 C400,668 200,690 0,735 Z" fill="#f5d6c3" opacity=".6"/>
    </svg>

    <h2 class="desc-title">Description</h2>
    <p class="desc-col desc-col--one"><span class="lead lead--yellow">After the fight.</span> Sessions for boxers and Muay Thai athletes focus on tired shoulders, tight hips and sore legs. Slow pressure and assisted stretching help the body recover between hard rounds, so you can train again sooner and move with more freedom in the ring.</p>
    <p class="desc-col desc-col--two"><span class="lead lead--purple">Above the city.</span> In the rooftop spa the pace slows down. Gentle rocking, warm palms and long stretches ease a busy mind and a stiff back. Nothing to prove, nothing to win, just time to breathe, rest and leave feeling lighter.</p>

    <div class="photo-circle photo-circle--desc" role="img" aria-label="Practitioner kneeling beside a client on a gym mat, guiding a leg stretch"></div>
    <p class="site-url site-url--desc">www.fernquiet.com</p>
    <span class="page-number page-number--right">3</span>
  </section>

</main>
</body>
</html>
```